Serenelle Aura Candle Box Package Design

Two box sizes:
14oz Candle in a box Gift Boxes - 4 x 4 x 6
4oz Candle in a box Gift Boxes - 3 x 3 x 3
Website: www.serenelleaura.com
IG: @serenelle.aura
My brand is a sophisticated brand with luxury candles made of coconut wax.  Serenelle Aura means bright life. Our candles represent hope and light.
You matter, you are worthy, powerful and beautiful!
Each candle is hand poured, vegan, environmentally conscious, uniquely scented and rooted in the importance of self care and community. We donate a percentage of our proceeds to organizations that seek to empower and enrich women.
At Serenelle Aura, we believe that positive energy can move mountains.
We strive to elevate that energy in every way possible. Our candles are handmade with confident positivity in mind - 100% vegan friendly, non-toxic and carefully crafted for optimal performance yet minimal impact on the environment.

```html
<!DOCTYPE html>
<html lang="en">
<head>
<meta charset="utf-8">
<title>Serenelle Aura – Candle Box</title>
<link href="https://fonts.googleapis.com/css2?family=Josefin+Sans:wght@300&family=Poppins:wght@400;500&display=swap" rel="stylesheet">
<style>
  :root{
    --bg:#dedede;
    --paper:#f6f6f5;
    --rose:#c4928c;
    --rose-deep:#b3837e;
    --sage:#8da293;
    --ink:#1d1b1b;
    --line:rgba(255,255,255,.85);
  }
  *{box-sizing:border-box;margin:0;padding:0}
  html,body{width:1200px;height:800px;overflow:hidden;background:var(--bg)}
  .canvas{position:relative;width:1200px;height:800px}
  .panel{position:absolute;top:140px;width:360px;height:520px;box-shadow:0 10px 30px rgba(0,0,0,.08)}
  .side-panel{left:240px;background:var(--rose);color:var(--ink);padding:34px 30px 0}
  .front-panel{left:600px;background:var(--paper)}

  .brand{display:flex;align-items:center;justify-content:center;gap:8px;font-family:'Josefin Sans',sans-serif;font-weight:300;text-transform:uppercase;color:var(--ink);white-space:nowrap}
  .side-brand{font-size:18px;letter-spacing:.12em}
  .dot{width:9px;height:9px;border-radius:50%;background:var(--ink)}
  .care-title{margin-top:34px;text-align:center;font-family:'Josefin Sans',sans-serif;font-weight:300;font-size:15px;letter-spacing:.14em}
  .care-list{margin-top:12px;font-family:'Poppins',sans-serif;font-size:8.5px;line-height:1.55;list-style:none}
  .care-list li::before{content:"•";margin-right:5px}
  .thanks{margin:16px auto 0;width:max-content;background:#eceaea;border-radius:10px;padding:4px 12px;font-family:'Poppins',sans-serif;font-weight:500;font-size:7.5px}
  .badges{display:flex;justify-content:space-between;margin-top:26px}
  .badge{display:flex;flex-direction:column;align-items:center;gap:5px;width:72px}
  .badge-mark{width:56px;height:56px;border:1px solid var(--line);border-radius:50%;background:rgba(255,255,255,.08)}
  .badge-label{font-family:'Poppins',sans-serif;font-size:7.5px;color:#fff;white-space:nowrap;text-align:center}
  .socials{display:flex;justify-content:center;gap:6px;margin-top:18px}
  .socials span{width:11px;height:11px;border-radius:50%;background:#fff}

  .front-top{height:350px;display:flex;align-items:center;justify-content:center;padding-top:30px}
  .front-brand{font-size:34px;letter-spacing:.06em}
  .front-band{height:130px;background:linear-gradient(90deg,var(--rose),var(--rose-deep));display:flex;flex-direction:column;align-items:center;justify-content:center;gap:10px}
  .front-badges{display:flex;gap:22px}
  .size{font-family:'Poppins',sans-serif;font-size:9px;color:#fff}
  .front-base{height:40px;background:var(--sage)}
</style>
</head>
<body>
<main class="canvas">
  <section class="panel side-panel">
    <div class="brand side-brand"><span class="dot"></span>Serenelle Aura</div>
    <h2 class="care-title">CANDLE CARE</h2>
    <ul class="care-list">
      <li>Place candle on a stable surface away from flammable objects before lighting</li>
      <li>Avoid burning candle for longer than 3-4 hours at a time</li>
      <li>Trim the wick to 1/4 in before each use</li>
      <li>Keep away from children and pets</li>
      <li>Never leave a burning candle unattended</li>
      <li>To prevent "tunneling" allow enough time for wax to melt completely to the edges of the container</li>
    </ul>
    <p class="thanks">WE HOPE YOU LOVE YOUR PURCHASE AS MUCH AS WE LOVED CREATING IT!</p>
    <div class="badges">
      <div class="badge"><div class="badge-mark" role="img" aria-label="Sparkle icon"></div><span class="badge-label">hand poured</span></div>
      <div class="badge"><div class="badge-mark" role="img" aria-label="Crossed flask icon"></div><span class="badge-label">paraben free</span></div>
      <div class="badge"><div class="badge-mark" role="img" aria-label="Hand with leaves icon"></div><span class="badge-label">clean burn</span></div>
      <div class="badge"><div class="badge-mark" role="img" aria-label="Crossed rabbit icon"></div><span class="badge-label">pet friendly</span></div>
    </div>
    <div class="socials"><span></span><span></span><span></span><span></span></div>
  </section>

  <section class="panel front-panel">
    <div class="front-top">
      <h1 class="brand front-brand">Serenelle Aura</h1>
    </div>
    <div class="front-band">
      <div class="front-badges">
        <div class="badge"><div class="badge-mark" role="img" aria-label="Globe with leaf icon"></div><span class="badge-label">eco-friendly</span></div>
        <div class="badge"><div class="badge-mark" role="img" aria-label="Coconut icon"></div><span class="badge-label">100% coconut wax</span></div>
        <div class="badge"><div class="badge-mark" role="img" aria-label="Droplet icon"></div><span class="badge-label">phthalate-free</span></div>
      </div>
      <p class="size">14oz | 396g</p>
    </div>
    <div class="front-base"></div>
  </section>
</main>
</body>
</html>
```